MORLIVEX Hemp based Pet Brand that growns it's own premium hemp and creates amazing pet products.

We need packaging designed for a new company based in South West Florida. We grow our own hemp with our other company Crest 4 Vale and use the harvest to make our hemp based pet products. Our initial products are pet treats that include Soft Chews and Calming Chews. The bags come in two different sizes. Regular bag being 7x10.25 inches and Small bag 4.25X6.25 inches. We also need a tincture box and label created. We want packaging that will catch the eye of the consumer and colors that compliment our logo. Dropper label size is 4x1.75 inches and the milligram of CBD is 1500. We have attached our manufacturers packaging and would like you to coppy everything other than their overall design and logo. Use default UPC and QR code, which we can replace later in the Ai file. Please see all the attached documents and please ask me if you have any questions. The final design should communicate a premium product that stand our from the rest. Something that catches the eye of the consumer by its premium appearance. Packaging is everything so I hope you can use your creative skills to create something special!

Target Market(s)

Pet owners

Font styles to use
Serif
Sans Serif

Colors
0054AA
0677BA
7BADD7
CADEEF
E8F1F8
0094D4
00A9DD
6FCCEA
C7EBF8
E9F6FB
EE7325
F08F49
F5BC92
FAE3D3
FDF4ED

Requirements
Must have
• Stand out design. Premium feel. Imagine shopping for something for your pet and seeing a brand that POPS and just looks like a good product because the packaging is so good.
Nice to have
• Modern mature feel
Should not have
• Cartoony feeling. Do not use baby blue everywhere. Do not include pictures of people in the packaging

```html
<!DOCTYPE html>
<html lang="en">
<head>
<meta charset="utf-8">
<title>MORLIVEX Canine Chews Packaging</title>
<link href="https://fonts.googleapis.com/css2?family=Josefin+Sans:wght@400&family=Quicksand:wght@500;600&family=Oswald:wght@300;500&display=swap" rel="stylesheet">
<style>
  :root{
    --backdrop:#d3d2cf;
    --white:#ffffff;
    --navy:#3d4768;
    --green:#2f9a5b;
    --red:#d83f49;
    --amber:#f0952f;
    --orange:#ee7f3a;
    --sky:#6fcaea;
  }
  *{box-sizing:border-box;margin:0;padding:0}
  html,body{width:1200px;height:900px;overflow:hidden}
  body{background:var(--backdrop);position:relative;font-family:"Quicksand",sans-serif}

  .bag{position:absolute;background:var(--white);border-radius:4px;overflow:hidden;
       box-shadow:0 6px 14px rgba(0,0,0,.12);color:var(--ink)}
  .bag--large{width:306px;height:440px;font-size:10px}
  .bag--small{width:193px;height:272px;font-size:6.3px}
  .bag--calming{left:307px;top:314px;--ink:var(--navy);--badge:var(--orange);--corner:var(--orange)}
  .bag--soft{left:614px;top:323px;--ink:var(--green);--badge:var(--orange);--corner:var(--orange)}
  .bag--calming-small{left:172px;top:482px;--ink:var(--red);--badge:var(--sky);--corner:var(--sky)}
  .bag--soft-small{left:871px;top:484px;--ink:var(--amber);--badge:var(--sky);--corner:var(--sky)}

  .bag__top{position:absolute;left:0;top:0;width:100%;height:11%;background:var(--ink)}
  .bag__flavor{position:absolute;left:3.5%;top:7.5%;width:21%;aspect-ratio:1;border-radius:50%;
       background:var(--badge);color:var(--white);font-family:"Oswald",sans-serif;
       display:flex;flex-direction:column;align-items:center;justify-content:center;
       transform:rotate(-18deg);line-height:1}
  .bag__flavor-main{font-weight:500;font-size:1.7em}
  .bag__flavor-sub{font-weight:300;font-size:1.3em}

  .bag__brand{position:absolute;left:0;top:16.5%;width:100%;display:flex;align-items:center;
       justify-content:center;gap:.5em;color:var(--navy);font-weight:600;font-size:1.15em;letter-spacing:.12em}
  .bag__brand-dot{width:1.1em;height:1.1em;border-radius:50%;background:var(--sky)}

  .bag__rule{position:absolute;left:25%;width:50%;height:1.5px;background:var(--ink)}
  .bag__rule--top{top:27.8%}
  .bag__rule--bottom{top:35.5%}
  .bag__title{position:absolute;left:0;top:28.8%;width:100%;text-align:center;
       font-family:"Josefin Sans",sans-serif;font-variant:small-caps;font-size:2.6em;letter-spacing:.04em;white-space:nowrap}
  .bag__subtitle{position:absolute;left:0;top:38%;width:100%;text-align:center;font-size:1.35em;font-weight:500}

  .bag__art{position:absolute;left:21%;top:46.5%;width:59%;height:37.5%;border-radius:44% 44% 48% 48%;
       background:radial-gradient(circle at 50% 45%, var(--white) 0%, color-mix(in srgb, var(--ink) 35%, white) 100%)}

  .bag__footer{position:absolute;left:0;bottom:0;width:100%;height:11%;background:var(--ink);
       color:var(--white);font-family:"Oswald",sans-serif;font-weight:300;font-size:.95em;
       padding:1.6% 0 0 3.5%;line-height:1.5;letter-spacing:.02em}
  .bag__corner{position:absolute;right:0;bottom:0;width:25%;height:20%;background:var(--corner);
       border-top-left-radius:70% 60%;color:var(--white);font-family:"Oswald",sans-serif;font-weight:300;
       text-align:right;padding-right:4%;font-size:1.2em;line-height:1.25;display:flex;flex-direction:column;justify-content:flex-end;padding-bottom:8%}
  .bag__paw{width:2.2em;height:2em;align-self:flex-end;margin-bottom:.6em}
</style>
</head>
<body>

<!-- Calming chews, regular -->
<section class="bag bag--large bag--calming">
  <div class="bag__top"></div>
  <div class="bag__flavor"><span class="bag__flavor-main">BACON</span><span class="bag__flavor-sub">FLAVOR</span></div>
  <div class="bag__brand"><span class="bag__brand-dot"></span>MORLIVEX</div>
  <div class="bag__rule bag__rule--top"></div>
  <h2 class="bag__title">Canine Calming Chews</h2>
  <div class="bag__rule bag__rule--bottom"></div>
  <p class="bag__subtitle">Full Spectrum Hemp Extract</p>
  <div class="bag__art" role="img" aria-label="Line illustration of a smiling golden retriever head"></div>
  <div class="bag__footer">718 C LANE, ORIVALE, FL 34120 &nbsp; TEL: (555) 019-2846<br>WWW.CANINELEAFWORKS.COM</div>
  <div class="bag__corner">
    <svg class="bag__paw" viewBox="0 0 22 20" fill="#fff"><ellipse cx="4" cy="8" rx="2.4" ry="3"/><ellipse cx="9" cy="4" rx="2.4" ry="3"/><ellipse cx="15" cy="4" rx="2.4" ry="3"/><ellipse cx="19" cy="9" rx="2.4" ry="3"/><ellipse cx="11.5" cy="14.5" rx="5.5" ry="4.5"/></svg>
    <span>NET CT. 60</span><span>NET WT. 10.5 OZ</span>
  </div>
</section>

<!-- Soft chews, regular -->
<section class="bag bag--large bag--soft">
  <div class="bag__top"></div>
  <div class="bag__flavor"><span class="bag__flavor-main">BACON</span><span class="bag__flavor-sub">FLAVOR</span></div>
  <div class="bag__brand"><span class="bag__brand-dot"></span>MORLIVEX</div>
  <div class="bag__rule bag__rule--top"></div>
  <h2 class="bag__title">Canine Soft Chews</h2>
  <div class="bag__rule bag__rule--bottom"></div>
  <p class="bag__subtitle">Full Spectrum Hemp Extract</p>
  <div class="bag__art" role="img" aria-label="Line illustration of a happy labrador head with tongue out"></div>
  <div class="bag__footer">718 C LANE, ORIVALE, FL 34120 &nbsp; TEL: (555) 019-2846<br>WWW.CANINELEAFWORKS.COM</div>
  <div class="bag__corner">
    <svg class="bag__paw" viewBox="0 0 22 20" fill="#fff"><ellipse cx="4" cy="8" rx="2.4" ry="3"/><ellipse cx="9" cy="4" rx="2.4" ry="3"/><ellipse cx="15" cy="4" rx="2.4" ry="3"/><ellipse cx="19" cy="9" rx="2.4" ry="3"/><ellipse cx="11.5" cy="14.5" rx="5.5" ry="4.5"/></svg>
    <span>NET CT. 60</span><span>NET WT. 10.5 OZ</span>
  </div>
</section>

<!-- Calming chews, small -->
<section class="bag bag--small bag--calming-small">
  <div class="bag__top"></div>
  <div class="bag__flavor"><span class="bag__flavor-main">BACON</span><span class="bag__flavor-sub">FLAVOR</span></div>
  <div class="bag__brand"><span class="bag__brand-dot"></span>MORLIVEX</div>
  <div class="bag__rule bag__rule--top"></div>
  <h2 class="bag__title">Canine Calming Chews</h2>
  <div class="bag__rule bag__rule--bottom"></div>
  <p class="bag__subtitle">Full Spectrum Hemp Extract</p>
  <div class="bag__art" role="img" aria-label="Line illustration of a smiling pomeranian head"></div>
  <div class="bag__footer">718 C LANE, ORIVALE, FL 34120 &nbsp; TEL: (555) 019-2846<br>WWW.CANINELEAFWORKS.COM</div>
  <div class="bag__corner">
    <svg class="bag__paw" viewBox="0 0 22 20" fill="#fff"><ellipse cx="4" cy="8" rx="2.4" ry="3"/><ellipse cx="9" cy="4" rx="2.4" ry="3"/><ellipse cx="15" cy="4" rx="2.4" ry="3"/><ellipse cx="19" cy="9" rx="2.4" ry="3"/><ellipse cx="11.5" cy="14.5" rx="5.5" ry="4.5"/></svg>
    <span>NET CT. 10</span><span>NET WT. 2 OZ</span>
  </div>
</section>

<!-- Soft chews, small -->
<section class="bag bag--small bag--soft-small">
  <div class="bag__top"></div>
  <div class="bag__flavor"><span class="bag__flavor-main">BACON</span><span class="bag__flavor-sub">FLAVOR</span></div>
  <div class="bag__brand"><span class="bag__brand-dot"></span>MORLIVEX</div>
  <div class="bag__rule bag__rule--top"></div>
  <h2 class="bag__title">Canine Soft Chews</h2>
  <div class="bag__rule bag__rule--bottom"></div>
  <p class="bag__subtitle">Full Spectrum Hemp Extract</p>
  <div class="bag__art" role="img" aria-label="Line illustration of a boston terrier head"></div>
  <div class="bag__footer">718 C LANE, ORIVALE, FL 34120 &nbsp; TEL: (555) 019-2846<br>WWW.CANINELEAFWORKS.COM</div>
  <div class="bag__corner">
    <svg class="bag__paw" viewBox="0 0 22 20" fill="#fff"><ellipse cx="4" cy="8" rx="2.4" ry="3"/><ellipse cx="9" cy="4" rx="2.4" ry="3"/><ellipse cx="15" cy="4" rx="2.4" ry="3"/><ellipse cx="19" cy="9" rx="2.4" ry="3"/><ellipse cx="11.5" cy="14.5" rx="5.5" ry="4.5"/></svg>
    <span>NET CT. 10</span><span>NET WT. 2 OZ</span>
  </div>
</section>

</body>
</html>
```